Spark Rally 2015

We're repeating the same promo in 2015 as a promo called Spark Rally for 2014. We simply need the look of the flyer changed for 2015. The concept is: we're better than the competition and we want to prove it. (without saying that) :)

Target Market(s)

This flyer will go to roofing contractors that do not use our company for their roofing needs. We would like them to try us and for that they get $500 off their order after buying $10K worth. We want an opportunity to prove to them that they will prefer us!

Industry/Entity Type

Promo

Colors
0356a4

Requirements
Must have
• Must not directly mention "competition"
Must be fairly reserved and male oriented (roofing contractors)
Title must be "Spark Rally in 2015"
Must have our logo & website www.pinecrestroofmart.com
Must have Terms and Conditions (with Expiration of Dec 31, 2016)
Nice to have
• A design that POPS!
Feel free to add things that you think will work
Be creative

```html
<!DOCTYPE html>
<html lang="en">
<head>
<meta charset="utf-8">
<title>Spark Rally in 2015 – Pinecrest Roof Mart</title>
<link rel="stylesheet" href="https://fonts.googleapis.com/css2?family=Archivo+Black&family=Arimo:wght@400;700&family=Tinos:wght@700&display=swap">
<style>
  :root {
    --brand-blue: #0356a4;
    --navy: #1b3f8e;
    --orange: #e07a12;
    --sky-edge: #5e9fee;
    --sky-mid: #9cc5f5;
    --sky-light: #e4f0fd;
    --ink: #000000;
    --white: #ffffff;
  }
  html, body {
    margin: 0;
    padding: 0;
    overflow: hidden;
    background: var(--white);
  }
  .flyer {
    position: relative;
    width: 927px;
    height: 1200px;
    overflow: hidden;
    background: radial-gradient(ellipse 70% 60% at 55% 48%, var(--sky-light) 0%, var(--sky-mid) 55%, var(--sky-edge) 100%);
    font-family: "Arimo", Arial, sans-serif;
  }
  .flyer > * { z-index: 1; }
  .headline {
    position: absolute;
    top: 20px;
    left: 0;
    width: 100%;
    margin: 0;
    text-align: center;
    font-family: "Archivo Black", "Arial Black", sans-serif;
    font-weight: 400;
    font-size: 67px;
    letter-spacing: 2px;
    line-height: 1;
    color: var(--brand-blue);
    text-shadow: 2px 3px 4px rgba(0, 0, 0, 0.35);
  }
  .offer {
    position: absolute;
    top: 108px;
    left: 0;
    width: 100%;
    margin: 0;
    text-align: center;
    font-family: "Archivo Black", "Arial Black", sans-serif;
    font-weight: 400;
    font-size: 52px;
    letter-spacing: 1px;
    line-height: 1;
    color: var(--orange);
  }
  .offer .amount { color: var(--ink); }
  .intro {
    position: absolute;
    top: 178px;
    left: 80px;
    width: 760px;
    margin: 0;
    text-align: center;
    font-weight: 700;
    font-size: 22.5px;
    line-height: 28px;
    color: var(--navy);
  }
  .hero-photo {
    position: absolute;
    left: 0;
    top: 248px;
    width: 515px;
    height: 864px;
    display: block;
    z-index: 0;
  }
  .brand-mark {
    position: absolute;
    left: 531px;
    top: 300px;
    width: 347px;
    height: 240px;
    display: flex;
    flex-direction: column;
    align-items: center;
    justify-content: center;
    gap: 16px;
  }
  .brand-mark .dot {
    width: 80px;
    height: 80px;
    border-radius: 50%;
    background: var(--brand-blue);
  }
  .brand-mark .name {
    font-weight: 700;
    font-size: 26px;
    white-space: nowrap;
    color: var(--brand-blue);
    letter-spacing: 0.5px;
  }
  .website {
    position: absolute;
    top: 562px;
    left: 531px;
    width: 347px;
    margin: 0;
    text-align: center;
    font-size: 18.5px;
    color: var(--orange);
  }
  .difference-title {
    position: absolute;
    top: 622px;
    left: 527px;
    margin: 0;
    font-family: "Tinos", "Times New Roman", serif;
    font-weight: 700;
    font-size: 24px;
    white-space: nowrap;
    color: var(--navy);
    text-decoration: underline;
    text-underline-offset: 3px;
  }
  .benefits {
    position: absolute;
    top: 660px;
    left: 581px;
    width: 344px;
    margin: 0;
    padding: 0;
    list-style: disc outside;
    font-weight: 700;
    font-size: 17px;
    line-height: 24px;
    color: var(--orange);
  }
  .benefits li.shift-1 { margin-left: 8px; }
  .benefits li.shift-2 { margin-left: 12px; }
  .promo-details {
    position: absolute;
    top: 870px;
    left: 633px;
    width: 294px;
    margin: 0;
    font-weight: 700;
    font-size: 17.5px;
    line-height: 23px;
    color: var(--navy);
  }
  .promo-details span { display: block; white-space: nowrap; }
  .promo-details .in-1 { padding-left: 40px; }
  .promo-details .in-2 { padding-left: 50px; }
  .promo-details .in-3 { padding-left: 56px; }
  .promo-details .in-4 { padding-left: 54px; }
  .terms {
    position: absolute;
    left: 0;
    top: 1112px;
    width: 100%;
    height: 88px;
    box-sizing: border-box;
    padding: 8px 8px 0 9px;
    margin: 0;
    background: var(--brand-blue);
    color: var(--white);
    font-size: 14.4px;
    line-height: 19px;
  }
  .terms strong { font-weight: 700; }
</style>
</head>
<body>
<main class="flyer">
  <svg class="hero-photo" role="img" aria-label="Photo of a smiling construction worker in a yellow hard hat, red ear muffs and an orange safety vest, arms crossed" viewBox="0 0 515 864" preserveAspectRatio="none">
    <defs>
      <linearGradient id="heroTone" x1="0" y1="0" x2="0" y2="1">
        <stop offset="0" stop-color="#c9b27a" stop-opacity="0.55"/>
        <stop offset="0.35" stop-color="#8a6a52" stop-opacity="0.75"/>
        <stop offset="0.6" stop-color="#d86a2a" stop-opacity="0.8"/>
        <stop offset="1" stop-color="#6a4f3a" stop-opacity="0.85"/>
      </linearGradient>
    </defs>
    <rect width="515" height="864" fill="url(#heroTone)"/>
  </svg>

  <h1 class="headline">SPARK RALLY in 2015!</h1>
  <h2 class="offer">RECEIVE A <span class="amount">$500</span> VOUCHER</h2>
  <p class="intro">After 40 years of servicing the Professional Contractor and Home Builder, we are confident that we can win you over!</p>

  <div class="brand-mark">
    <span class="dot"></span>
    <span class="name">PINECREST ROOF MART</span>
  </div>
  <p class="website">www.pinecrestroofmart.com</p>

  <h3 class="difference-title">THE PINECREST DIFFERENCE</h3>
  <ul class="benefits">
    <li>Triple check system for accurate delivery</li>
    <li>Inventory of Major Brands</li>
    <li class="shift-1">Take-off Services</li>
    <li class="shift-2">New fleet monitored by TrackLine®</li>
    <li class="shift-2">Finance Options</li>
    <li class="shift-2">Marketing programs to increase your back log</li>
    <li class="shift-2">Online Bill Pay</li>
  </ul>

  <p class="promo-details">
    <span>New customers who have</span>
    <span>purchased less than $2,000</span>
    <span>in the past 6 months will be</span>
    <span>issued a $500 voucher upon</span>
    <span class="in-1">purchasing $10,000, to</span>
    <span class="in-2">be used for additional</span>
    <span class="in-3">purchases at Pinecrest</span>
    <span class="in-4">Roof Mart. Limit one</span>
    <span class="in-4">voucher per customer.</span>
  </p>

  <p class="terms"><strong>Terms and Conditions</strong>: Voucher is to be used for future purchases but may not be used to pay off any previous balance on current account. No one time purchasers. This promotion and your participation in it is void where prohibited by law, rules, or regulations. Pinecrest Roof Mart reserves the right the cancel, suspend, limit, and/or modify this promotion at any time for any reason, without notice. Expires December 31, 2016. All rights reserved by Pinecrest Roof Mart.</p>
</main>
</body>
</html>
```